Business Card Design Project

We are looking for a new business card design for a Drilling company in WA, Australia.

We are in between offices, however require a design in the meantime due to some upcoming events with our basic information.

The Logo for our company is Blue and Grey and would like this colour scheme throughout.

We are quite a new company so would like a memorable design that stands out and communicates a strong commitment to safety, quality of work and performance.

The company name is Ironbark Boring Group (IBG)

The details to be included are as follows:

Gavin Thorley
Managing Director
m.0481639207
e.gavin@ibgpty.com.au

Martin Thorley
Director
m.0419852637
e.martin@ibgpty.com.au

Industry/Entity Type

Events

Requirements
Must have
• Under the Logo, we would like 'Western Australia'

```html
<!DOCTYPE html>
<html lang="en">
<head>
<meta charset="utf-8">
<title>Ironbark Boring Group – Business Card</title>
<link rel="stylesheet" href="https://fonts.googleapis.com/css2?family=Open+Sans:wght@400;600;700;800&display=swap">
<style>
  :root {
    --brand-blue: #0b3f8c;
    --brand-grey: #7d7f83;
    --map-grey: #e6e7e9;
    --card-white: #ffffff;
    --backdrop: #f2f3f5;
    --text-dark: #2c3140;
    --text-body: #4a4f5c;
  }
  * { box-sizing: border-box; margin: 0; padding: 0; }
  html, body {
    width: 1200px;
    height: 900px;
    overflow: hidden;
    background: var(--backdrop);
    font-family: "Open Sans", Arial, sans-serif;
  }
  .canvas {
    position: relative;
    width: 1200px;
    height: 900px;
  }
  .card {
    position: absolute;
    left: 250px;
    width: 700px;
    height: 400px;
    background: var(--card-white);
    overflow: hidden;
    box-shadow: 0 2px 10px rgba(0, 0, 0, 0.12);
  }
  .card--front { top: 40px; }
  .card--back { top: 460px; }

  .brand {
    position: absolute;
    z-index: 2;
  }
  .card--front .brand { left: 150px; top: 55px; }
  .card--back .brand { left: 90px; top: 65px; }

  .wordmark {
    display: flex;
    align-items: center;
    gap: 14px;
    color: var(--brand-blue);
    font-weight: 800;
    line-height: 1;
  }
  .wordmark__mark {
    width: 14px;
    height: 14px;
    background: var(--brand-blue);
    flex: none;
  }
  .wordmark__initials {
    font-size: 64px;
    letter-spacing: 1px;
  }
  .wordmark__name {
    font-size: 22px;
    line-height: 1.1;
    text-transform: uppercase;
    letter-spacing: 1px;
    border-left: 3px solid var(--brand-blue);
    padding-left: 12px;
  }
  .brand__region {
    margin-top: 10px;
    padding-left: 28px;
    color: var(--brand-grey);
    font-size: 15px;
    font-weight: 600;
    letter-spacing: 4px;
    text-transform: uppercase;
  }

  .map-region {
    position: absolute;
  }
  .map-region--australia-front {
    left: 300px; top: 225px; width: 190px; height: 140px;
    background: var(--map-grey);
    border-radius: 18px 40px 30px 24px;
  }
  .map-region--wa-front {
    left: 290px; top: 240px; width: 90px; height: 110px;
    background: var(--brand-blue);
    border-radius: 22px 4px 4px 30px;
  }
  .map-region--australia-back {
    left: -20px; top: 10px; width: 280px; height: 210px;
    background: var(--map-grey);
    opacity: 0.6;
    border-radius: 40px 70px 60px 30px;
  }
  .map-region--wa-back {
    left: 500px; top: 30px; width: 200px; height: 300px;
    background: var(--brand-blue);
    border-radius: 70px 0 0 40px;
  }

  .contacts {
    position: absolute;
    left: 90px;
    top: 245px;
    display: flex;
    gap: 60px;
    z-index: 2;
  }
  .contact { width: 170px; }
  .contact__name {
    color: var(--brand-blue);
    font-weight: 700;
    font-size: 16px;
  }
  .contact__role {
    color: var(--text-dark);
    font-size: 13px;
    margin-top: 3px;
  }
  .contact__details {
    margin-top: 28px;
    color: var(--text-body);
    font-size: 13px;
    line-height: 1.45;
    white-space: nowrap;
  }
</style>
</head>
<body>
<main class="canvas">
  <section class="card card--front" aria-label="Business card front">
    <div class="brand">
      <div class="wordmark">
        <span class="wordmark__mark" aria-hidden="true"></span>
        <span class="wordmark__initials">IBG</span>
        <span class="wordmark__name">Ironbark<br>Boring<br>Group</span>
      </div>
      <p class="brand__region">Western Australia</p>
    </div>
    <div class="map-region map-region--australia-front" role="img" aria-label="Map of Australia in light grey"></div>
    <div class="map-region map-region--wa-front" role="img" aria-label="Western Australia highlighted in blue on the map of Australia"></div>
  </section>

  <section class="card card--back" aria-label="Business card back">
    <div class="map-region map-region--australia-back" role="img" aria-label="Faint map of Australia in the background"></div>
    <div class="map-region map-region--wa-back" role="img" aria-label="Large map of Western Australia in blue"></div>
    <div class="brand">
      <div class="wordmark">
        <span class="wordmark__mark" aria-hidden="true"></span>
        <span class="wordmark__initials">IBG</span>
        <span class="wordmark__name">Ironbark<br>Boring<br>Group</span>
      </div>
      <p class="brand__region">Western Australia</p>
    </div>
    <div class="contacts">
      <div class="contact">
        <p class="contact__name">Gavin Thorley</p>
        <p class="contact__role">Managing Director</p>
        <p class="contact__details">m.0481639207<br>e.gavin@ibgpty.com.au</p>
      </div>
      <div class="contact">
        <p class="contact__name">Martin Thorley</p>
        <p class="contact__role">Director</p>
        <p class="contact__details">m.0419852637<br>e.martin@ibgpty.com.au</p>
      </div>
    </div>
  </section>
</main>
</body>
</html>
```